Permanent Makeup (cosmetics salon) Brochure

We need a 2-4 sites brochure for our Permanent Makeup (cosmetics salon). Our company is based in Austria / Vienna. -> Our homepage is www.mk-lorenzhuber.at
This brochure should show which treatments we provide ot our customers.

I've uploaded our old brochure, the content (text) would be nearly the same (look form "Must Haves", pics have to be new (look uploaded pics)
The old brochure is to dark. -> look for our homepage maybe you can make it like this

Target Market(s)

woman, age 25-70 years who wants to have permanent makeup on eyebrows, lips or eyeliner

Industry/Entity Type

Beauty Salon

Requirements
Must have
• pics which are uploaded.

*This text (somithing about our business)
"Für Frau Lorenzhuber ist Permanent Makeup ein Kunsthandwerk. Das Team von MK-Lorenzhuber ist spezialisiert auf natürliches Permanent Makeup damit der individuelle Typ jeder Kundin am schönsten zum Ausdruck kommt."

*We do this treatments: (english)
+ Augenbrauen Microblading (eyebrows)
+ Augenbrauen Permanent Makeup (eyebrows2)
+ Lidstrich Permanent Makeup (eyeliner)
+ Lip Blushing (lips)
+ Lippen Permanent Makeup (lips2)

* Our addresses (2 locations)
Wien
Kerngasse 7b/12, 1010 Wien
Tel: 01/5827316

Villach
Birkenhofweg 24, 9524 St. Ulrich
Tel: 0676/3158940

Mail: info@mk-lorenzhuber.at
www.mk-lorenzhuber.at

```html
<!DOCTYPE html>
<html lang="de">
<head>
<meta charset="utf-8">
<title>MK-Lorenzhuber – Permanent Makeup Treatments</title>
<link rel="stylesheet" href="https://fonts.googleapis.com/css2?family=Merriweather:wght@400;700&family=Montserrat:wght@500;600&display=swap">
<style>
  :root {
    --gold-dark: #b8861b;
    --gold: #f1c232;
    --gold-soft: #f7dc8a;
    --ink: #3d3d3d;
    --bullet: #9a9372;
    --band: rgba(70, 72, 78, 0.88);
    --white: #ffffff;
    --photo-a: #8c97a3;
    --photo-b: #d9b8a3;
  }
  * { margin: 0; padding: 0; box-sizing: border-box; }
  html, body { width: 849px; height: 1200px; overflow: hidden; background: #ffffff; }
  .brochure-page {
    position: relative; width: 849px; height: 1200px; overflow: hidden;
    font-family: "Merriweather", Georgia, serif; color: var(--ink);
  }
  .hero-photo {
    position: absolute; left: 0; top: 0; width: 849px; height: 640px;
    background: linear-gradient(100deg, #6f7d8c 0%, var(--photo-a) 35%, var(--photo-b) 60%, #caa48e 80%, #9aa3ac 100%);
  }
  .footer-photo {
    position: absolute; left: 0; top: 990px; width: 849px; height: 210px;
    background: linear-gradient(90deg, #b9a799 0%, #e6e2de 40%, #f2e8e0 65%, #d8b39c 85%, #c79f89 100%);
  }
  .content-swoosh { position: absolute; left: 0; top: 0; width: 849px; height: 1200px; }
  .detail-circle {
    position: absolute; border-radius: 50%; border: 9px solid var(--gold);
  }
  .detail-circle--eye {
    left: 85px; top: 360px; width: 254px; height: 254px;
    background: radial-gradient(circle at 50% 55%, #7a5a3c 0%, #c9a58c 35%, #e7cdbb 70%);
  }
  .detail-circle--lips {
    left: 490px; top: 587px; width: 310px; height: 310px;
    background: radial-gradient(circle at 50% 50%, #d98a83 0%, #e8b3a4 40%, #f1d3c3 75%);
  }
  .treatments { position: absolute; left: 60px; top: 625px; }
  .treatments-title {
    font-family: "Montserrat", Arial, sans-serif; font-weight: 600;
    font-size: 40px; line-height: 46px; letter-spacing: 1px; color: var(--gold-dark);
  }
  .treatments-title span { display: block; color: var(--gold); }
  .treatment-list { list-style: none; margin-top: 22px; }
  .treatment-list li {
    display: flex; align-items: center; font-size: 22px; height: 45px;
  }
  .treatment-list li::before {
    content: ""; width: 16px; height: 16px; border-radius: 50%;
    background: var(--bullet); margin-right: 18px; flex: none;
  }
  .contact-band {
    position: absolute; left: 0; top: 1025px; width: 849px; height: 113px;
    background: linear-gradient(90deg, var(--band) 0%, var(--band) 70%, rgba(70,72,78,0.55) 100%);
    color: var(--white); font-size: 17px; line-height: 27px;
  }
  .location { position: absolute; top: 16px; }
  .location--wien { left: 62px; }
  .location--villach { left: 388px; }
  .location-name { color: var(--gold); font-weight: 700; }
  .web-band {
    position: absolute; left: 0; top: 1138px; width: 849px; height: 62px;
    background: linear-gradient(90deg, var(--gold) 0%, var(--gold) 70%, rgba(241,194,50,0.6) 100%);
    color: var(--white); font-size: 17px; display: flex; align-items: center; padding-left: 62px;
  }
  .web-band .divider { margin: 0 22px; }
</style>
</head>
<body>
<main class="brochure-page">
  <div class="hero-photo" role="img" aria-label="Portrait photo of a woman with groomed eyebrows and natural lips"></div>
  <div class="footer-photo" role="img" aria-label="Soft beauty photo behind the contact area"></div>

  <svg class="content-swoosh" viewBox="0 0 849 1200" aria-hidden="true">
    <path d="M0 585 C 230 545 520 520 849 470 L849 1025 L0 1025 Z" fill="var(--gold-soft)" opacity="0.6"/>
    <path d="M0 600 C 240 560 520 540 849 500 L849 1025 L0 1025 Z" fill="#ffffff"/>
    <path d="M0 600 C 240 560 520 540 849 500" fill="none" stroke="var(--gold)" stroke-width="6"/>
  </svg>

  <div class="detail-circle detail-circle--eye" role="img" aria-label="Close-up photo of an eye with eyeliner and eyebrow"></div>
  <div class="detail-circle detail-circle--lips" role="img" aria-label="Close-up photo of lips with lip blushing"></div>

  <section class="treatments">
    <h1 class="treatments-title">WE DO THIS <span>TREATMENTS</span></h1>
    <ul class="treatment-list">
      <li>Augenbrauen Microblading</li>
      <li>Augenbrauen Permanent Makeup</li>
      <li>Lidstrich Permanent Makeup</li>
      <li>Lip Blushing</li>
      <li>Lippen Permanent Makeup</li>
    </ul>
  </section>

  <footer>
    <div class="contact-band">
      <div class="location location--wien">
        <div class="location-name">Wien</div>
        <div>Kerngasse 7b/12, 1010 Wien</div>
        <div>Tel: 01/5827316</div>
      </div>
      <div class="location location--villach">
        <div class="location-name">Villach</div>
        <div>Birkenhofweg 24, 9524 St. Ulrich</div>
        <div>Tel: 0676/3158940</div>
      </div>
    </div>
    <div class="web-band">
      <span>info@mk-lorenzhuber.at</span><span class="divider">|</span><span>www.mk-lorenzhuber.at</span>
    </div>
  </footer>
</main>
</body>
</html>
```